Management Consultancy needs sharp professional services showcased in a brochure

We are a management consultancy specializing on contract management and conflict avoidance services requiring a professional brochure showcasing our services to prospective clients.

Attached are a selection of existing stationary and the colour scheme.

Further details on our company can be found at www.velto-advisory-partners.com
Updates

Preference is for bi-fold, however, innovative tri-fold will be considered. Added Monday, August 7, 2017

Target Market(s)

Construction companies, consultants, developers, oil and gas service providers, NGO's, SME's.

Industry/Entity Type

Management

Requirements
Must have
• High degree of professionalism with eye catching, sharp detail. No frils.
• Colour scheme as per the attachments
• Font as per attachments - Century Gothic
• Details of our company and services
Nice to have
• Open to ideas, thinking along the lines of a car brochure type design.
• Bi-fold preferred, by trifold accepted if innovative.
Should not have
• Remove reference to the United Arab Emirates.
• No cartoon/clipart photos.

```html
<!DOCTYPE html>
<html lang="en">
<head>
<meta charset="utf-8">
<title>Velto Advisory – Contract and Conflict Advisory Brochure</title>
<link rel="stylesheet" href="https://fonts.googleapis.com/css2?family=Questrial&family=Raleway:wght@300;400;600;700&display=swap">
<style>
  :root {
    --navy: #242c42;
    --red: #b1272d;
    --steel: #3f5a7a;
    --steel-dark: #283e5a;
    --paper: #f3f3f4;
    --grey-photo: #7d7f83;
    --ink: #2b3040;
    --stage: #9f9f9f;
    --bullet-light: #dfe6ef;
  }
  * { margin: 0; padding: 0; box-sizing: border-box; }
  html, body { width: 1200px; height: 1200px; overflow: hidden; }
  body { background: var(--stage); font-family: "Raleway", sans-serif; color: var(--ink); position: relative; }

  .spread { position: absolute; left: 124px; width: 953px; height: 476px; display: flex; }
  .spread--cover { top: 110px; }
  .spread--inside { top: 614px; }
  .page { position: relative; width: 476.5px; height: 476px; overflow: hidden; }
  .page svg.page__art { position: absolute; inset: 0; width: 100%; height: 100%; }

  /* Back cover */
  .back { background: var(--navy); }
  .back__footer { position: absolute; left: 98px; width: 282px; top: 425px; text-align: center; color: #d6d9e2; }
  .back__countries { font-size: 6px; letter-spacing: .2px; padding-bottom: 4px; border-bottom: 1px solid #8a90a3; }
  .back__countries .dot { color: var(--red); margin: 0 4px; }
  .back__contact { font-size: 5.6px; margin-top: 5px; white-space: nowrap; }
  .back__contact b { font-weight: 600; }

  /* Front cover */
  .front { background: linear-gradient(120deg, #fff 40%, #ececee 100%); }
  .front__title { position: absolute; left: 26px; top: 72px; font-family: "Questrial", sans-serif; font-weight: 400; font-size: 23px; line-height: 28px; color: #fff; letter-spacing: .6px; }
  .front__brand { position: absolute; left: 228px; top: 34px; width: 128px; height: 52px; background: #f1f1f2; display: flex; align-items: center; justify-content: center; gap: 6px; font-family: "Questrial", sans-serif; font-size: 13px; color: var(--navy); }
  .front__brand .mark { width: 8px; height: 8px; border-radius: 50%; background: var(--red); }
  .front__web { position: absolute; left: 178px; top: 418px; font-family: "Questrial", sans-serif; font-size: 13.5px; color: var(--navy); }
  .front__web b { font-weight: 700; font-family: "Raleway", sans-serif; font-size: 12.5px; }

  /* Inside shared */
  .heading { position: absolute; left: 44px; top: 40px; font-family: "Raleway", sans-serif; font-weight: 300; font-size: 24px; color: #fff; }
  .rule { position: absolute; top: 70px; height: 2px; }
  .copy { position: absolute; font-size: 7px; line-height: 8.6px; font-weight: 400; }
  .copy--light { color: var(--bullet-light); }

  .bullet { width: 4px; height: 4px; flex: none; margin-top: 2px; background: currentColor; }

  .about__list { position: absolute; left: 44px; top: 104px; width: 390px; display: grid; grid-template-columns: 1fr 1fr; row-gap: 3px; column-gap: 14px; font-size: 7px; color: var(--bullet-light); list-style: none; }
  .about__list li { display: flex; align-items: flex-start; gap: 6px; border-bottom: 1px solid rgba(255,255,255,.2); padding-bottom: 1px; }

  .services__lead { position: absolute; left: 248px; top: 82px; width: 188px; font-size: 8.8px; line-height: 10.6px; color: var(--navy); }
  .card { position: absolute; left: 44px; width: 390px; height: 114px; display: flex; }
  .card__label { width: 62px; background: var(--red); position: relative; }
  .card__label span { position: absolute; left: 50%; top: 50%; transform: translate(-50%,-50%) rotate(-90deg); font-family: "Questrial", sans-serif; font-size: 12px; line-height: 13px; color: #fff; text-align: center; white-space: nowrap; }
  .card__photo { width: 142px; background: linear-gradient(90deg, #e9e9ec, #f7f7f8 50%, #e2e2e6); }
  .card__list { flex: 1; background: var(--navy); list-style: none; padding: 22px 10px 0 16px; color: #e3e6ee; font-size: 6.8px; line-height: 8px; }
  .card__list li { display: flex; gap: 5px; margin-bottom: 8px; }
</style>
</head>
<body>

<section class="spread spread--cover">
  <div class="page back">
    <div class="back__footer">
      <p class="back__countries">UNITED KINGDOM<span class="dot">•</span>IRELAND<span class="dot">•</span>BRAZIL</p>
      <p class="back__contact">Velto Advisory Limited · <b>E:</b> info@velto-advisory-partners.com · www.<b>velto-advisory-partners</b>.com</p>
    </div>
  </div>

  <div class="page front">
    <svg class="page__art" viewBox="0 0 476 476" preserveAspectRatio="none">
      <defs>
        <linearGradient id="rustFade" x1="0" y1="0" x2="1" y2="1">
          <stop offset="0" stop-color="#c99686"/>
          <stop offset=".55" stop-color="#b9604e"/>
          <stop offset="1" stop-color="#b1402f"/>
        </linearGradient>
      </defs>
      <polygon points="0,45 218,45 158,234 0,234" fill="var(--navy)"/>
      <polygon points="0,234 158,234 134,320 0,320" fill="url(#rustFade)" role="img" aria-label="Red-tinted photo of an empty meeting room"/>
      <polygon points="236,101 476,101 476,375 146,375" fill="url(#rustFade)" role="img" aria-label="Red-tinted photo of a businessman standing at an office window"/>
      <line x1="230" y1="0" x2="136" y2="441" stroke="var(--navy)" stroke-width="1.4"/>
    </svg>
    <h1 class="front__title">THE<br>CONTRACT<br>AND<br>CONFLICT<br>ADVISORY</h1>
    <div class="front__brand"><span class="mark"></span>Velto Advisory</div>
    <p class="front__web">www.<b>velto-advisory-partners</b>.com</p>
  </div>
</section>

<section class="spread spread--inside">
  <div class="page about" style="background:var(--paper)">
    <svg class="page__art" viewBox="0 0 476 476" preserveAspectRatio="none">
      <defs>
        <linearGradient id="steelFade" x1="0" y1="0" x2="1" y2="1">
          <stop offset="0" stop-color="var(--steel)"/>
          <stop offset="1" stop-color="var(--steel-dark)"/>
        </linearGradient>
        <linearGradient id="globeFade" x1="0" y1="0" x2="1" y2="0">
          <stop offset="0" stop-color="#3d3f44"/>
          <stop offset="1" stop-color="#8c8e92"/>
        </linearGradient>
      </defs>
      <polygon points="0,0 476,0 476,178 0,238" fill="url(#steelFade)" role="img" aria-label="Blue-tinted photo of a city skyline through office windows"/>
      <polygon points="0,238 476,178 0,395" fill="url(#globeFade)" role="img" aria-label="Black and white photo of a desk globe"/>
      <polygon points="330,476 476,476 476,418" fill="var(--grey-photo)" role="img" aria-label="Photo of a meeting table"/>
    </svg>
    <h2 class="heading">About Us</h2>
    <span class="rule" style="left:44px;width:272px;background:#6d7f96"></span>
    <span class="rule" style="left:324px;width:110px;background:var(--red)"></span>

    <p class="copy copy--light" style="left:44px;top:82px;width:392px">We are an experienced contract and conflict advisory providing global contract performance solutions and conflict management to:</p>
    <ul class="about__list">
      <li><span class="bullet"></span>international development organisations;</li>
      <li><span class="bullet"></span>oil and gas industry; and</li>
      <li><span class="bullet"></span>construction industry;</li>
      <li><span class="bullet"></span>government sectors.</li>
    </ul>
    <p class="copy copy--light" style="left:44px;top:134px;width:396px">Observing the standard of consultancy services and magnitude of contractual engagements and conflicts, we see the opportunity to make things better, better engagements, better awareness, better performance, which all lead to better value in terms of financial benefit and relationship maintenance. We firmly believe in party success in a non litigious environment.</p>
    <p class="copy copy--light" style="left:44px;top:176px;width:352px">Our services are uniquely delivered through our integrated management consultancy model, with a single point of contact and responsibility, and focused attention to detail. We provide advisory services and solutions resolving past and current claims, and in doing so, preparing our clients for a conflict free future based on our core principles of integrity, equality and strength, ensuring compliance and experience at an intimate professional level. We aim to have our clients feel our principles in our presence and in our advisories, giving the service which is deserved.</p>
    <p class="copy copy--light" style="left:118px;top:238px;width:150px">Our clients range from leading global companies, international contractors to government bodies and authorities.</p>
    <p class="copy" style="left:278px;top:284px;width:160px;color:var(--ink)">Velto Advisory is more than just a professional advisory consultancy; we are an integrated professional team with deep domain expertise, industry knowledge and the ability to work across multiple jurisdictions supported by a wide professional network.</p>
    <p class="copy" style="left:156px;top:348px;width:282px;color:var(--ink)">We forge strong client partnerships and in doing so, we develop and maintain these relationships through performance and delivery of professional services which create and maximise value for our clients.</p>
    <p class="copy" style="left:73px;top:386px;width:346px;color:var(--ink)">Through our unique approach to contract and conflict management, we want the best for our clients to ensure that contract integrity, compliance and performance is maintained with the upmost faith, based around our principles.</p>
    <p class="copy" style="left:44px;top:422px;width:290px;color:var(--ink)">"If value, whether financial or relationship is not achieved, then we are not finished, we have only just begun."</p>
  </div>

  <div class="page services" style="background:#f6f6f7">
    <svg class="page__art" viewBox="0 0 476 476" preserveAspectRatio="none">
      <defs>
        <linearGradient id="handsFade" x1="0" y1="0" x2="1" y2="1">
          <stop offset="0" stop-color="#3a3b3f"/>
          <stop offset="1" stop-color="#b8b9bc"/>
        </linearGradient>
        <linearGradient id="tableFade" x1="0" y1="0" x2="1" y2="0">
          <stop offset="0" stop-color="#d9d9dc"/>
          <stop offset="1" stop-color="#8e8f93"/>
        </linearGradient>
      </defs>
      <polygon points="0,0 375,0 0,178" fill="url(#handsFade)" role="img" aria-label="Black and white photo of hands over documents with a pen"/>
      <polygon points="0,330 476,170 476,476 0,476" fill="url(#tableFade)" role="img" aria-label="Soft grey photo of a boardroom table"/>
    </svg>
    <h2 class="heading">Our Services</h2>
    <span class="rule" style="left:128px;width:188px;background:var(--navy)"></span>
    <span class="rule" style="left:323px;width:110px;background:var(--red)"></span>
    <p class="services__lead">Velto Advisory is more than just a professional advisory consultancy; we are an integrated professional team with deep domain expertise, industry knowledge and the ability to work across multiple jurisdictions supported by a wide professional network.</p>
    <p class="copy" style="left:80px;top:162px;width:330px;color:var(--ink)">Velto Advisory is more than just a professional advisory consultancy; we are an integrated professional team with deep domain expertise, industry knowledge and the ability to work across multiple jurisdictions supported by a wide professional network.</p>

    <div class="card" style="top:200px">
      <div class="card__label"><span>CONFLICT<br>ADVISORY</span></div>
      <div class="card__photo" role="img" aria-label="Photo of two hands joining navy puzzle pieces"></div>
      <ul class="card__list">
        <li><span class="bullet"></span>Restoration and Mediation Services.</li>
        <li><span class="bullet"></span>Shuttle Diplomacy Services and In Persona Intermediary Services.</li>
        <li><span class="bullet"></span>Negotiation Support Services.</li>
        <li><span class="bullet"></span>Workplace/Corporate Mediation Services.</li>
      </ul>
    </div>

    <div class="card" style="top:333px">
      <div class="card__label"><span>CONTRACT<br>ADVISORY</span></div>
      <div class="card__photo" role="img" aria-label="Photo of two hands joining navy puzzle pieces"></div>
      <ul class="card__list">
        <li><span class="bullet"></span>Restoration and Mediation Services.</li>
        <li><span class="bullet"></span>Shuttle Diplomacy Services and In Persona Intermediary Services.</li>
        <li><span class="bullet"></span>Negotiation Support Services.</li>
        <li><span class="bullet"></span>Workplace/Corporate Mediation Services.</li>
      </ul>
    </div>
  </div>
</section>

</body>
</html>
```